Refresh of The Marston Collective business card

Update business card design using existing primary logo. Names, numbers, etc. are too hard to read on current design.

Target Market(s)

We are a CPA firm.

Industry/Entity Type

Accountant

Contact Information for Business Card

update current card

Colors
0355a3
3176b5
85acd3
0792cd

Requirements
Must have
• Easier to read phone numbers and names
• Use existing logo
Nice to have
• We love our color scheme and current TMC logo. But the names and phone numbers are too small and card just look old and stale.

```html
<!DOCTYPE html>
<html lang="en">
<head>
<meta charset="utf-8">
<title>The Marston Collective – Business Card</title>
<link href="https://fonts.googleapis.com/css2?family=Cinzel:wght@500;600&family=EB+Garamond:wght@400;500&display=swap" rel="stylesheet">
<style>
  :root {
    --page-bg: #e6e6e6;
    --card-white: #ffffff;
    --brand-blue: #0355a3;
    --brand-mid: #3176b5;
    --brand-light: #85acd3;
    --band-dark: #3c3c3c;
    --band-dark-2: #5a5a5a;
    --ink: #2a2a2a;
    --rule-grey: #b9b9b9;
    --back-center: #6e6e6e;
    --back-edge: #2f2f2f;
    --back-line: rgba(255,255,255,0.55);
    --back-ink: #ffffff;
  }
  * { box-sizing: border-box; margin: 0; padding: 0; }
  html, body { width: 1200px; height: 1200px; overflow: hidden; }
  body {
    background: var(--page-bg);
    display: flex; flex-direction: column; align-items: center; justify-content: center;
    gap: 56px;
    font-family: "EB Garamond", Georgia, serif;
  }
  .card {
    position: relative; width: 900px; height: 514px; overflow: hidden;
    box-shadow: 0 6px 18px rgba(0,0,0,0.22);
  }

  /* ---------- Front ---------- */
  .card-front { background: var(--card-white); }
  .front-top-stripe { position: absolute; top: 0; left: 0; right: 0; height: 8px; background: var(--brand-blue); }
  .front-bottom-rule { position: absolute; left: 0; right: 38px; bottom: 26px; height: 1px; background: var(--rule-grey); }
  .front-side-rule { position: absolute; right: 38px; top: 280px; bottom: 26px; width: 1px; background: var(--rule-grey); }

  .brand-lockup {
    position: absolute; top: 48px; left: 250px;
    display: flex; align-items: center; gap: 22px;
  }
  .brand-mark {
    width: 112px; height: 112px; border-radius: 50%;
    background: radial-gradient(circle at 40% 35%, var(--brand-mid), var(--brand-blue) 70%);
  }
  .brand-words { display: flex; flex-direction: column; }
  .brand-name {
    font-family: "Cinzel", "Times New Roman", serif; font-weight: 600;
    font-size: 34px; letter-spacing: 1px; color: var(--brand-blue); line-height: 1.1;
    padding-bottom: 8px; border-bottom: 1.5px solid var(--ink);
  }
  .brand-tagline {
    margin-top: 7px; font-family: "Cinzel", serif; font-weight: 500;
    font-size: 12.5px; letter-spacing: 2.6px; text-transform: uppercase; color: var(--ink);
  }

  .name-band-accent { position: absolute; left: 0; top: 216px; width: 126px; height: 62px; background: var(--brand-mid); }
  .name-band {
    position: absolute; left: 146px; right: 38px; top: 216px; height: 62px;
    background: linear-gradient(90deg, var(--band-dark-2), var(--band-dark));
    display: flex; align-items: center; justify-content: flex-end; padding-right: 30px;
  }
  .holder-name {
    font-family: "Cinzel", "Times New Roman", serif; font-weight: 600;
    font-size: 33px; color: #ffffff; letter-spacing: 0.5px;
  }

  .contact-list {
    position: absolute; left: 40px; top: 312px; list-style: none;
    display: flex; flex-direction: column; gap: 13px;
  }
  .contact-list::before {
    content: ""; position: absolute; left: 12px; top: 10px; bottom: 10px; width: 1px; background: var(--brand-light);
  }
  .contact-item { position: relative; display: flex; align-items: center; gap: 20px; font-size: 23px; color: var(--ink); line-height: 1; }
  .contact-icon { width: 25px; height: 25px; flex: none; background: var(--card-white); }

  /* ---------- Back ---------- */
  .card-back { background: radial-gradient(ellipse at 50% 50%, var(--back-center), var(--back-edge) 80%); }
  .frame-line { position: absolute; background: var(--back-line); }
  .frame-top { top: 38px; left: 0; width: 560px; height: 1px; }
  .frame-left { top: 0; left: 38px; width: 1px; height: 300px; }
  .frame-bottom { bottom: 38px; right: 0; width: 560px; height: 1px; }
  .frame-right { bottom: 0; right: 38px; width: 1px; height: 300px; }

  .back-lockup {
    position: absolute; top: 170px; left: 50%; transform: translateX(-50%);
    display: flex; align-items: center; gap: 22px;
  }
  .back-mark { width: 118px; height: 118px; border-radius: 50%; background: #ffffff; flex: none; }
  .back-lockup .brand-name { color: var(--back-ink); border-bottom-color: var(--back-line); }
  .back-lockup .brand-tagline { color: var(--back-ink); }
  .back-url {
    position: absolute; top: 406px; left: 0; right: 0; text-align: center;
    font-size: 22px; font-weight: 500; color: var(--back-ink); letter-spacing: 0.3px;
  }
</style>
</head>
<body>

<section class="card card-front" aria-label="Business card front">
  <div class="front-top-stripe"></div>

  <div class="brand-lockup">
    <div class="brand-mark"></div>
    <div class="brand-words">
      <span class="brand-name">The Marston Collective</span>
      <span class="brand-tagline">Certified Public Accountants</span>
    </div>
  </div>

  <div class="name-band-accent"></div>
  <div class="name-band"><span class="holder-name">DANIEL J. MARSTON, CPA</span></div>

  <ul class="contact-list">
    <li class="contact-item">
      <svg class="contact-icon" viewBox="0 0 26 26" aria-label="Office phone"><circle cx="13" cy="13" r="11.5" fill="#fff" stroke="#3176b5" stroke-width="1.5"/><path d="M8 11 Q13 7 18 11 L17 12.5 L15 12 L15 11 Q13 10 11 11 L11 12 L9 12.5 Z M9 14 H17 V18 H9 Z" fill="#0355a3"/></svg>
      555.210.4318
    </li>
    <li class="contact-item">
      <svg class="contact-icon" viewBox="0 0 26 26" aria-label="Direct line"><circle cx="13" cy="13" r="11.5" fill="#fff" stroke="#3176b5" stroke-width="1.5"/><path d="M9 8 L11 8 L12 11 L10.5 12 Q12 15 14 15.5 L15 14 L18 15 L18 17 Q17 18.5 15 18 Q9 16 8 10 Q8 8.5 9 8 Z" fill="#0355a3"/></svg>
      555.210.4392
    </li>
    <li class="contact-item">
      <svg class="contact-icon" viewBox="0 0 26 26" aria-label="Mobile"><circle cx="13" cy="13" r="11.5" fill="#fff" stroke="#3176b5" stroke-width="1.5"/><rect x="9.5" y="6.5" width="7" height="13" rx="1.2" fill="none" stroke="#0355a3" stroke-width="1.6"/><circle cx="13" cy="17" r="0.9" fill="#0355a3"/></svg>
      555.307.1846
    </li>
    <li class="contact-item">
      <svg class="contact-icon" viewBox="0 0 26 26" aria-label="Email"><circle cx="13" cy="13" r="11.5" fill="#fff" stroke="#3176b5" stroke-width="1.5"/><rect x="7" y="9" width="12" height="8.5" fill="#0355a3"/><path d="M7 9 L13 14 L19 9" fill="none" stroke="#fff" stroke-width="1.2"/></svg>
      dan@marstoncollective.com
    </li>
    <li class="contact-item">
      <svg class="contact-icon" viewBox="0 0 26 26" aria-label="Website"><circle cx="13" cy="13" r="11.5" fill="#fff" stroke="#3176b5" stroke-width="1.5"/><circle cx="13" cy="13" r="6" fill="none" stroke="#0355a3" stroke-width="1.4"/><path d="M7 13 H19 M13 7 Q10 13 13 19 M13 7 Q16 13 13 19" fill="none" stroke="#0355a3" stroke-width="1.1"/></svg>
      www.marstoncollective.com
    </li>
  </ul>

  <div class="front-side-rule"></div>
  <div class="front-bottom-rule"></div>
</section>

<section class="card card-back" aria-label="Business card back">
  <div class="frame-line frame-top"></div>
  <div class="frame-line frame-left"></div>
  <div class="frame-line frame-bottom"></div>
  <div class="frame-line frame-right"></div>

  <div class="back-lockup">
    <div class="back-mark"></div>
    <div class="brand-words">
      <span class="brand-name">The Marston Collective</span>
      <span class="brand-tagline">Certified Public Accountants</span>
    </div>
  </div>

  <p class="back-url">www.marstoncollective.com</p>
</section>

</body>
</html>
```